Brantley Advisory Group provides support for renewable energy projects to utilities and suppliers

I need a professional looking business card that is both simple and elegant and unique. My clients are mostly large organizations not individuals. I am a consultant with my own company that is small but would like to give clients the impression I am larger. Smart grid, fiber optics, software, field hardware, distribution automation, substation automation, operations, energy storage/batteries, microgrids, customer service, strategy/roadmaps, conservation, Automated Metering Infrastruture (AMI or smart meters) are all areas of focus.

Target Market(s)

Utilities, suppliers, governmental agencies involved in energy. All types of energy especially natural gas and electrical. Especially renewable energy or green projects.

Contact Information for Business Card

Name - Mark Brantley Cell Phone - 425.318.2746 Email - mbrantley@brantleyag-example.com
Company - Brantley Advisory Group (logo) Title - Principal

Font styles to use
Serif
Sans Serif

Colors

Designer to choose colors to be used in the design.

Requirements
Must have
• Simple and professional and powerful.
• Unique/creative design.
Nice to have
• Utilize color scheme to accent logo colors. Maybe some geometric pattern on edge of card with color.
Should not have
• Busy, complicated, traditional

```html
<!DOCTYPE html>
<html lang="en">
<head>
<meta charset="utf-8">
<title>Brantley Advisory Group – Business Card</title>
<link href="https://fonts.googleapis.com/css2?family=Montserrat:wght@400;600;700&display=swap" rel="stylesheet">
<style>
  :root {
    --page-bg: #ecebe8;
    --card-dark: #404042;
    --card-light: #ffffff;
    --ink-white: #ffffff;
    --brand-navy: #1f3a93;
    --brand-green: #4f8a2b;
    --ink-grey: #7a7a7a;
    --mark-grey: #cfcfcf;
  }
  * { margin: 0; padding: 0; box-sizing: border-box; }
  html, body {
    width: 1200px; height: 900px; overflow: hidden;
    background: var(--page-bg);
    font-family: "Montserrat", Arial, sans-serif;
  }
  .card {
    position: absolute;
    left: 311px;
    width: 577px;
    height: 329px;
  }
  .card--front { top: 98px; background: var(--card-dark); }
  .card--back { top: 472px; background: var(--card-light); border: 1px solid #e2e1de; }

  .brand {
    position: absolute;
    display: flex;
    align-items: center;
  }
  .brand__square {
    flex: none;
    border-radius: 6px;
  }
  .brand__name {
    font-weight: 600;
    line-height: 1.15;
  }

  .card--front .brand { left: 132px; top: 112px; gap: 22px; }
  .card--front .brand__square {
    width: 64px; height: 64px;
    border: 4px solid var(--mark-grey);
  }
  .card--front .brand__name { color: var(--ink-white); font-size: 32px; }

  .card--back .brand { left: 43px; top: 30px; gap: 16px; }
  .card--back .brand__square {
    width: 44px; height: 44px;
    border: 3px solid var(--brand-navy);
  }
  .card--back .brand__name { color: var(--brand-navy); font-size: 24px; }

  .contact {
    position: absolute;
    left: 42px;
    top: 198px;
    color: var(--ink-grey);
    font-size: 14.5px;
  }
  .contact__name {
    font-weight: 600;
    font-size: 14.5px;
    letter-spacing: 0.3px;
    line-height: 18px;
  }
  .contact__first { color: var(--brand-navy); }
  .contact__last { color: var(--brand-green); }
  .contact__title { line-height: 18px; letter-spacing: 0.3px; }
  .contact__rule {
    width: 25px; height: 2px;
    background: var(--brand-navy);
    margin: 6px 0 7px;
  }
  .contact__line {
    display: flex;
    align-items: center;
    gap: 9px;
    height: 24px;
    letter-spacing: 0.4px;
  }
  .contact__icon { width: 16px; height: 16px; flex: none; }
</style>
</head>
<body>

<section class="card card--front">
  <div class="brand">
    <span class="brand__square"></span>
    <span class="brand__name">Brantley<br>Advisory Group</span>
  </div>
</section>

<section class="card card--back">
  <div class="brand">
    <span class="brand__square"></span>
    <span class="brand__name">Brantley<br>Advisory Group</span>
  </div>

  <div class="contact">
    <p class="contact__name"><span class="contact__first">MARK</span> <span class="contact__last">BRANTLEY</span></p>
    <p class="contact__title">Principal</p>
    <div class="contact__rule"></div>
    <p class="contact__line">
      <svg class="contact__icon" viewBox="0 0 24 24" aria-hidden="true">
        <path fill="#1f3a93" d="M6.6 10.8a15.1 15.1 0 0 0 6.6 6.6l2.2-2.2c.3-.3.7-.4 1-.2 1.1.4 2.3.6 3.6.6.6 0 1 .4 1 1V20c0 .6-.4 1-1 1A17 17 0 0 1 3 4c0-.6.4-1 1-1h3.5c.6 0 1 .4 1 1 0 1.3.2 2.5.6 3.6.1.3 0 .7-.2 1z"/>
      </svg>
      425.318.2746
    </p>
    <p class="contact__line">
      <svg class="contact__icon" viewBox="0 0 24 24" aria-hidden="true">
        <rect x="2" y="5" width="20" height="14" rx="1.5" fill="#1f3a93"/>
        <path d="M3 6.5l9 6.5 9-6.5" fill="none" stroke="#ffffff" stroke-width="1.6"/>
      </svg>
      mbrantley@brantleyag-example.com
    </p>
  </div>
</section>

</body>
</html>
```